Homemaking training schools needs a Business Card design

Designer, Hello!

No special requirements, good-looking enough.
--------------------------------------------------------------------------

Name: Marcus Liao
Chairman
Tel: 0574-57418263
Mobile: 13852247106
Email: kelvory@mailpond.com
Web: www.tqb2031.com
Add: No.258, LinfengJie, DaoyueQu, Ningbo, Zhejiang

LOGO
Ningbo TQB Homemaking Training School

Target Market(s)

pregnant women, mothers, infants, the elderly and families, including cleaning, cooking, nursing training.

Industry/Entity Type

Business

Contact Information for Business Card

Name: Marcus Liao
Chairman
Tel: 0574-57418263
Mobile: 13852247106
Email: kelvory@mailpond.com
Web: www.tqb2031.com

LOGO

Font styles to use
Serif
Sans Serif
Decorative

Requirements
Nice to have
• Feels: clean, specifications, safety, comfort, warmth and happiness.

```html
<!DOCTYPE html>
<html lang="en">
<head>
<meta charset="utf-8">
<title>TianQiBao Business Card</title>
<link href="https://fonts.googleapis.com/css2?family=Open+Sans:wght@400;600;700&display=swap" rel="stylesheet">
<style>
  :root {
    --stage: #000000;
    --card: #333438;
    --brand-blue: #1f76c6;
    --brand-pink: #e5157f;
    --text-light: #f2f2f2;
    --muted: #56585c;
    --divider: rgba(255,255,255,0.16);
  }
  * { margin: 0; padding: 0; box-sizing: border-box; }
  html, body { width: 1200px; height: 900px; overflow: hidden; background: var(--stage); }
  body { position: relative; font-family: "Open Sans", Arial, sans-serif; }

  .card {
    position: absolute;
    top: 271px;
    width: 457px;
    height: 281px;
    border-radius: 14px;
    background: var(--card);
  }
  .card--front { left: 137px; }
  .card--back { left: 626px; }

  /* front */
  .front-mark {
    position: absolute;
    left: 40px;
    top: 84px;
    width: 122px;
    text-align: center;
  }
  .front-mark__dot {
    display: block;
    width: 26px; height: 26px;
    margin: 0 auto 14px;
    border-radius: 50%;
    background: var(--brand-pink);
  }
  .front-mark__name {
    color: var(--brand-blue);
    font-weight: 600;
    font-size: 21px;
  }
  .front-divider {
    position: absolute;
    left: 191px;
    top: 85px;
    width: 1px;
    height: 160px;
    background: linear-gradient(to bottom, transparent, var(--divider), transparent);
  }
  .contact {
    position: absolute;
    left: 241px;
    top: 56px;
    color: var(--text-light);
    font-size: 12.5px;
    line-height: 19px;
  }
  .contact__name { color: var(--brand-pink); font-weight: 700; font-size: 16px; line-height: 22px; }
  .contact__title { margin-bottom: 9px; }
  .contact__address { margin-bottom: 11px; }
  .contact__list { list-style: none; }
  .contact__list li { display: flex; align-items: center; gap: 6px; }
  .contact__list svg { width: 9px; height: 9px; fill: var(--brand-pink); flex: none; }

  /* back */
  .brand {
    position: absolute;
    left: 0; right: 0;
    top: 82px;
    text-align: center;
  }
  .brand__dot {
    display: block;
    width: 16px; height: 16px;
    margin: 0 auto 10px;
    border-radius: 50%;
    background: var(--brand-pink);
  }
  .brand__name {
    color: var(--brand-blue);
    font-weight: 600;
    font-size: 38px;
    line-height: 44px;
  }
  .brand__tagline {
    display: flex;
    align-items: center;
    justify-content: center;
    gap: 6px;
    margin-top: 0;
    color: var(--muted);
    font-size: 13px;
  }
  .brand__tagline::before,
  .brand__tagline::after {
    content: "";
    width: 58px;
    height: 1px;
    background: var(--muted);
  }
</style>
</head>
<body>
  <section class="card card--front">
    <div class="front-mark">
      <span class="front-mark__dot"></span>
      <span class="front-mark__name">TianQiBao</span>
    </div>
    <div class="front-divider"></div>
    <div class="contact">
      <p class="contact__name">Marcus Liao</p>
      <p class="contact__title">Chairman</p>
      <p class="contact__address">No.258, LinfengJie,<br>DaoyueQu, Ningbo, Zhejiang</p>
      <ul class="contact__list">
        <li><svg viewBox="0 0 10 10"><path d="M2 0.5l2 2-1 1.2c.7 1.4 1.8 2.5 3.2 3.2l1.2-1 2 2-1.2 1.6C4.5 9.3.7 5.5.4 1.7z"/></svg>0574-57418263</li>
        <li><svg viewBox="0 0 10 10"><path d="M2.5 0h5v10h-5zM3.5 1v7h3V1z"/></svg>13852247106</li>
        <li><svg viewBox="0 0 10 10"><path d="M0 2h10v6H0zM0 2l5 3.5L10 2v1L5 6.5 0 3z"/></svg>kelvory@mailpond.com</li>
        <li><svg viewBox="0 0 10 10"><circle cx="5" cy="5" r="5"/></svg>www.tqb2031.com</li>
      </ul>
    </div>
  </section>

  <section class="card card--back">
    <div class="brand">
      <span class="brand__dot"></span>
      <p class="brand__name">TianQiBao</p>
      <p class="brand__tagline">Training &amp; Services</p>
    </div>
  </section>
</body>
</html>
```